Business card design needed

Hello, I Need a business card for a company that specialises in providing contract management services for civil construction projects - roads, bridges etc.
I do have a logo that i produced for PLOVER Civilworks however it probably needs a little work, the circles dont have defined edges, i was thinking the colours should reflect the dry interior of Australia progressing out to the colours of the ocean as you move towards the East.... that was my thinking anyway!
Target Market(s)
Professional people generally 30+ yrs old who need professional services to deliver contracts in a high risk environment
Industry/Entity Type
Construction
Contact Information for Business Card
PLOVER Civilworks
Darren Pollock - Director and Principal Engineer
Registered Professional Engineer of Queensland
Phone 0491 265 807
Email darren@plovercivilworks.com.au
ABN 48 213 670 194
Logo Text
PLOVER Civilworks
Logo styles of interest
Pictorial/Combination Logo
Wordmark Logo
Lettermark Logo
Look and feel

```html
<!DOCTYPE html>
<html lang="en">
<head>
<meta charset="utf-8">
<title>PLOVER Civilworks – Business Card</title>
<link rel="stylesheet" href="https://fonts.googleapis.com/css2?family=Sorts+Mill+Goudy&display=swap">
<style>
  :root {
    --backdrop: #2b2b2b;
    --card: #f7f7f7;
    --ink: #1c1c1c;
    --brand-ink: #3a3a3a;
    --teal: #14847c;
    --red: #b5302a;
    --yellow: #f2cf0c;
  }
  * { margin: 0; padding: 0; box-sizing: border-box; }
  html, body {
    width: 1200px;
    height: 900px;
    overflow: hidden;
    background: var(--backdrop);
    font-family: "Sorts Mill Goudy", Georgia, serif;
    color: var(--ink);
  }
  .canvas {
    position: relative;
    width: 1200px;
    height: 900px;
  }
  .card {
    position: absolute;
    width: 560px;
    height: 320px;
    background: var(--card);
    box-shadow: 0 10px 30px rgba(0,0,0,0.5);
  }
  .card--front { left: 90px; top: 90px; }
  .card--back { left: 550px; top: 480px; }

  /* Front */
  .brand {
    position: absolute;
    display: flex;
    align-items: center;
    gap: 14px;
  }
  .card--front .brand { left: 70px; top: 200px; }
  .brand__dot {
    width: 30px;
    height: 30px;
    border-radius: 50%;
    background: var(--teal);
  }
  .brand__name {
    font-size: 34px;
    color: var(--brand-ink);
    letter-spacing: 0.5px;
  }

  /* Back */
  .holder {
    position: absolute;
    left: 40px;
    top: 70px;
  }
  .holder__name {
    font-size: 34px;
    line-height: 1;
    letter-spacing: 1px;
  }
  .holder__title {
    margin-top: 10px;
    font-size: 14px;
    line-height: 1.2;
    color: var(--teal);
  }
  .card--back .brand { left: 40px; top: 180px; gap: 10px; }
  .card--back .brand__dot { width: 22px; height: 22px; }
  .card--back .brand__name { font-size: 20px; }
  .abn {
    position: absolute;
    left: 40px;
    bottom: 34px;
    font-size: 16px;
  }
  .abn__label { color: var(--teal); }
  .contact {
    position: absolute;
    right: 36px;
    top: 74px;
    text-align: right;
    font-size: 15px;
    line-height: 1.3;
  }
  .contact__label {
    color: var(--teal);
    font-size: 14px;
    letter-spacing: 0.5px;
  }
  .contact__value + .contact__label { margin-top: 6px; }
  .contact__email { margin-top: 30px; }
</style>
</head>
<body>
<main class="canvas">
  <section class="card card--front" aria-label="Card front">
    <div class="brand">
      <span class="brand__dot"></span>
      <span class="brand__name">PLOVER Civilworks</span>
    </div>
  </section>

  <section class="card card--back" aria-label="Card back">
    <div class="holder">
      <h1 class="holder__name">Darren Pollock</h1>
      <p class="holder__title">Director and Principal Engineer Registered<br>Professional Engineer of Queensland</p>
    </div>
    <div class="brand">
      <span class="brand__dot"></span>
      <span class="brand__name">PLOVER Civilworks</span>
    </div>
    <p class="abn"><span class="abn__label">ABN</span> 48 213 670 194</p>
    <div class="contact">
      <p class="contact__label">PHONE</p>
      <p class="contact__value">0491 265 807</p>
      <p class="contact__label">EMAIL</p>
      <p class="contact__value contact__email">darren@plovercivilworks.com.au</p>
    </div>
  </section>
</main>
</body>
</html>
```